Banner Ad Design Project

We are a SEO company and need a banner design for our new service, the highlights being:

- Pay Per Performance SEO service
- Guaranteed Frobly page 1 ranking
- Only $197 per month (+ performance bonus)

Can be all on one static banner or made into an animated GIF - designers choice...

Site URL (not up yet) will be RankLoft.com (by Velbrin) - this is a spinoff site of our existing business, Velbrin LLC - logo attached and should be included on the banner.

Industry/Entity Type

Business

Requirements
Must have
• Banner delivered in multiple sizes:
- 200 x 200
- 250 x 250
- 300 x 250
- 336 x 280
- 468 x 60
- 728 x 90
- 120 x 600
- 160 x 600

```html
<!DOCTYPE html>
<html lang="en">
<head>
<meta charset="utf-8">
<title>Velbrin – Pay Per Performance SEO banner set</title>
<link rel="stylesheet" href="https://fonts.googleapis.com/css2?family=Roboto+Condensed:wght@700&display=swap">
<style>
  :root {
    --navy: #1f3f8f;
    --corner: #1d4aa3;
    --corner-light: #3b73c9;
    --price: #8cc63f;
    --mark: #9ccb3b;
    --card: #f3f4f5;
    --stage-top: #e9eaeb;
    --stage-bottom: #dcdddf;
  }
  * { box-sizing: border-box; margin: 0; padding: 0; }
  html, body { width: 929px; height: 1200px; overflow: hidden; }
  body {
    position: relative;
    background: linear-gradient(180deg, var(--stage-top), var(--stage-bottom));
    font-family: "Roboto Condensed", "Arial Narrow", sans-serif;
    font-weight: 700;
    color: var(--navy);
  }
  .banner {
    position: absolute;
    background: var(--card);
    box-shadow: 0 3px 6px rgba(0,0,0,.35);
    overflow: hidden;
    display: flex;
    flex-direction: column;
    --fs: 24px; --cut: 46px;
  }
  .banner::before, .banner::after {
    content: ""; position: absolute; width: var(--cut); height: var(--cut);
  }
  .banner::before {
    top: 0; left: 0;
    background: radial-gradient(circle at 100% 100%, transparent 68%, var(--corner) 70%, var(--corner-light) 100%);
  }
  .banner::after {
    bottom: 0; right: 0;
    background: radial-gradient(circle at 0 0, transparent 68%, var(--corner) 70%, var(--corner-light) 100%);
  }
  .logo { display: flex; align-items: center; gap: 8px; position: relative; z-index: 1; }
  .logo-dot { flex: none; border-radius: 50%; background: var(--mark); width: var(--dot); height: var(--dot); }
  .logo-name { font-size: var(--name); line-height: 1; color: var(--corner); letter-spacing: .5px; }
  .logo.stacked { flex-direction: column; gap: 10px; }
  .points { display: flex; flex-direction: column; position: relative; z-index: 1; }
  .point { display: flex; align-items: center; justify-content: space-between; font-size: var(--fs); line-height: 1.15; }
  .point.stacked { flex-direction: column; align-items: flex-start; }
  .point.stacked .tick { align-self: center; }
  .price { font-size: var(--fs); line-height: 1.15; }
  .price em { font-style: normal; color: var(--price); }
  .tick { flex: none; width: var(--tick); height: calc(var(--tick) * .8); }
  .strip { flex-direction: row; align-items: center; justify-content: space-between; }
  .strip .points { align-items: flex-end; text-align: right; }
  .strip .point { justify-content: flex-end; gap: 8px; }
</style>
</head>
<body>
<svg width="0" height="0" style="position:absolute">
  <defs>
    <linearGradient id="tick-fill" x1="0" y1="0" x2="0" y2="1">
      <stop offset="0" stop-color="#b8e26a"/><stop offset="1" stop-color="#5fa81e"/>
    </linearGradient>
    <symbol id="tick" viewBox="0 0 50 40">
      <path d="M2 20 L10 13 L20 22 L41 2 L48 9 L20 37 Z" fill="url(#tick-fill)" stroke="#4c8f17" stroke-width="1.5" stroke-linejoin="round"/>
    </symbol>
  </defs>
</svg>

<!-- 250 x 250 -->
<section class="banner" style="left:32px;top:24px;width:301px;height:300px;padding:14px 10px 0 9px;--fs:24px;--tick:52px;--dot:64px;--name:48px;">
  <div class="logo" style="justify-content:center;"><span class="logo-dot"></span><span class="logo-name">Velbrin</span></div>
  <div class="points" style="margin-top:22px;gap:10px;">
    <div class="point"><span>Pay Per Performance<br>SEO service</span><svg class="tick"><use href="#tick"/></svg></div>
    <div class="point"><span>Frobly guaranteed<br>page 1 ranking</span><svg class="tick"><use href="#tick"/></svg></div>
    <p class="price">Only <em>$197</em> per month<br>(+ performance bonus)</p>
  </div>
</section>

<!-- 200 x 200 -->
<section class="banner" style="left:352px;top:24px;width:240px;height:240px;padding:10px 10px 0 7px;--fs:19px;--tick:42px;--dot:44px;--name:38px;--cut:38px;">
  <div class="logo" style="justify-content:center;"><span class="logo-dot"></span><span class="logo-name">Velbrin</span></div>
  <div class="points" style="margin-top:16px;gap:8px;">
    <div class="point"><span>Pay Per Performance<br>SEO service</span><svg class="tick"><use href="#tick"/></svg></div>
    <div class="point"><span>Guaranteed Frobly<br>page 1 ranking</span><svg class="tick"><use href="#tick"/></svg></div>
    <p class="price">Only <em>$197</em> per month<br>(+ performance bonus)</p>
  </div>
</section>

<!-- 160 x 600 -->
<section class="banner" style="left:602px;top:26px;width:196px;height:721px;padding:24px 10px 0 19px;--fs:26px;--tick:58px;--dot:70px;--name:36px;">
  <div class="logo stacked"><span class="logo-dot"></span><span class="logo-name">Velbrin</span></div>
  <div class="points" style="margin-top:30px;gap:36px;">
    <div class="point stacked"><span>Pay Per<br>Performance<br>SEO service</span><svg class="tick" style="margin-top:18px"><use href="#tick"/></svg></div>
    <div class="point stacked"><span>Guaranteed<br>Frobly page 1<br>ranking</span><svg class="tick" style="margin-top:18px"><use href="#tick"/></svg></div>
    <p class="price" style="line-height:1.3">Only <em>$197</em><br>per month<br>(+performance<br>bonus)</p>
  </div>
</section>

<!-- 120 x 600 -->
<section class="banner" style="left:446px;top:271px;width:145px;height:719px;padding:22px 6px 0 10px;--fs:19px;--tick:46px;--dot:66px;--name:34px;--cut:40px;">
  <div class="logo stacked"><span class="logo-dot"></span><span class="logo-name">Velbrin</span></div>
  <div class="points" style="margin-top:46px;gap:40px;">
    <div class="point stacked"><span style="line-height:1.45">Pay Per<br>Performance<br>SEO service</span><svg class="tick" style="margin-top:12px"><use href="#tick"/></svg></div>
    <div class="point stacked"><span style="line-height:1.45">Guaranteed<br>Frobly page 1<br>ranking</span><svg class="tick" style="margin-top:12px"><use href="#tick"/></svg></div>
    <p class="price" style="line-height:1.45;margin-top:32px;font-size:18px">Only <em>$197</em><br>per month<br>(+performance<br>bonus)</p>
  </div>
</section>

<!-- 300 x 250 -->
<section class="banner" style="left:32px;top:346px;width:360px;height:300px;padding:14px 30px 0 44px;--fs:23px;--tick:54px;--dot:64px;--name:46px;">
  <div class="logo" style="justify-content:center;"><span class="logo-dot"></span><span class="logo-name">Velbrin</span></div>
  <div class="points" style="margin-top:20px;gap:10px;">
    <div class="point" style="justify-content:flex-start;gap:8px"><span>Pay Per Performance<br>SEO service</span><svg class="tick"><use href="#tick"/></svg></div>
    <div class="point" style="justify-content:flex-start;gap:22px"><span>Guaranteed Frobly<br>page 1 ranking</span><svg class="tick"><use href="#tick"/></svg></div>
    <p class="price">Only <em>$197</em> per month<br>(+ performance bonus)</p>
  </div>
</section>

<!-- 336 x 280 -->
<section class="banner" style="left:32px;top:654px;width:403px;height:336px;padding:14px 12px 0 14px;--fs:29px;--tick:62px;--dot:76px;--name:56px;">
  <div class="logo" style="justify-content:center;"><span class="logo-dot"></span><span class="logo-name">Velbrin</span></div>
  <div class="points" style="margin-top:18px;gap:14px;">
    <div class="point"><span>Pay Per Performance SEO<br>service</span><svg class="tick"><use href="#tick"/></svg></div>
    <div class="point"><span>Guaranteed Frobly page<br>1 ranking</span><svg class="tick"><use href="#tick"/></svg></div>
    <p class="price">Only <em>$197</em> per month<br>(+ performance bonus)</p>
  </div>
</section>

<!-- 468 x 60 -->
<section class="banner strip" style="left:32px;top:995px;width:562px;height:72px;padding:0 22px 0 16px;--fs:15px;--tick:26px;--dot:42px;--name:34px;--cut:28px;">
  <div class="logo"><span class="logo-dot"></span><span class="logo-name">Velbrin</span></div>
  <div class="points">
    <div class="point"><span>Pay Per Performance SEO service</span><svg class="tick"><use href="#tick"/></svg></div>
    <div class="point"><span>Guaranteed Frobly page 1 ranking</span><svg class="tick"><use href="#tick"/></svg></div>
    <p class="price" style="margin-right:34px">Only <em>$197</em> per month (+ performance bonus)</p>
  </div>
</section>

<!-- 728 x 90 -->
<section class="banner strip" style="left:32px;top:1074px;width:874px;height:108px;padding:0 30px 0 24px;--fs:23px;--tick:44px;--dot:66px;--name:54px;--cut:40px;">
  <div class="logo"><span class="logo-dot"></span><span class="logo-name">Velbrin</span></div>
  <div class="points">
    <div class="point"><span>Pay Per Performance SEO service</span><svg class="tick"><use href="#tick"/></svg></div>
    <div class="point"><span>Guaranteed Frobly page 1 ranking</span><svg class="tick"><use href="#tick"/></svg></div>
    <p class="price" style="margin-right:52px">Only <em>$197</em> per month (+ performance bonus)</p>
  </div>
</section>
</body>
</html>
```